Salt Water Delivery Company Business Card Design

We are a company that delivers natural saltwater (from the ocean) to aquarium companies, restaurants and home marine tanks. I would like a new business card to suit.

Must include Name, company name, abn, contact number and website as well as logo (see attached).

Looking for a design that stands out, has a clean but unique appearance.

Double and single sided entries welcome

Industry/Entity Type

Business

Requirements
Must have
• Logo

```html
<!DOCTYPE html>
<html lang="en">
<head>
<meta charset="utf-8">
<title>Brine Run Business Card</title>
<link href="https://fonts.googleapis.com/css2?family=Ubuntu:wght@400;500;700&display=swap" rel="stylesheet">
<style>
  :root {
    --page-top: #f4f4f4;
    --page-bottom: #d6d6d6;
    --ocean-light: #1f9be0;
    --ocean-mid: #1976cf;
    --ocean-deep: #4b55b0;
    --sky-pale: #eaf6fc;
    --sky-soft: #bfe3f6;
    --wave-navy: #2a3f9e;
    --text-light: #ffffff;
    --text-soft: #e3f1fb;
  }
  * { box-sizing: border-box; margin: 0; padding: 0; }
  html, body {
    width: 1200px;
    height: 900px;
    overflow: hidden;
  }
  body {
    background: linear-gradient(180deg, var(--page-top), var(--page-bottom));
    font-family: "Ubuntu", sans-serif;
    display: flex;
    align-items: center;
    justify-content: center;
  }
  .business-card {
    position: relative;
    width: 840px;
    height: 480px;
    overflow: hidden;
    background: linear-gradient(160deg, var(--ocean-light) 0%, var(--ocean-mid) 45%, var(--ocean-deep) 100%);
    box-shadow: 0 18px 40px rgba(0, 0, 0, 0.25);
  }
  .water-surface {
    position: absolute;
    inset: 0;
    width: 100%;
    height: 100%;
  }
  .holder {
    position: absolute;
    left: 64px;
    top: 136px;
    color: var(--text-light);
  }
  .holder-name {
    font-size: 46px;
    font-weight: 500;
    line-height: 1.1;
  }
  .holder-position {
    font-size: 24px;
    font-weight: 500;
    margin-top: 4px;
  }
  .contact-list {
    position: absolute;
    left: 64px;
    top: 246px;
    display: grid;
    grid-template-columns: 108px auto;
    row-gap: 2px;
    font-size: 17px;
    color: var(--text-soft);
    line-height: 1.2;
  }
  .contact-list dt, .contact-list dd { display: block; }
  .contact-list .gap { margin-top: 12px; }
  .brand {
    position: absolute;
    right: 70px;
    top: 300px;
    display: flex;
    align-items: center;
    gap: 14px;
  }
  .brand-dot {
    width: 22px;
    height: 22px;
    border-radius: 50%;
    background: var(--text-light);
  }
  .brand-name {
    font-size: 44px;
    font-weight: 500;
    color: var(--text-light);
  }
</style>
</head>
<body>
  <article class="business-card">
    <svg class="water-surface" viewBox="0 0 840 480" role="img" aria-label="Illustrated ocean wave surface with bubbles across the top of the card">
      <defs>
        <linearGradient id="sky" x1="0" y1="0" x2="1" y2="0">
          <stop offset="0" stop-color="var(--sky-soft)"/>
          <stop offset="1" stop-color="var(--sky-pale)"/>
        </linearGradient>
        <linearGradient id="crest" x1="0" y1="0" x2="1" y2="0">
          <stop offset="0" stop-color="var(--wave-navy)" stop-opacity="0.9"/>
          <stop offset="1" stop-color="var(--ocean-light)" stop-opacity="0.6"/>
        </linearGradient>
      </defs>
      <path d="M0,52 C140,40 260,48 380,70 C500,92 600,128 700,150 C760,162 810,162 840,158 L840,186 C790,192 730,186 660,170 C560,148 470,110 360,96 C230,80 110,86 0,92 Z" fill="url(#crest)"/>
      <path d="M0,0 H840 V158 C800,162 760,160 700,150 C600,128 500,92 380,70 C260,48 140,40 0,52 Z" fill="url(#sky)"/>
    </svg>

    <header class="holder">
      <h1 class="holder-name">Name Surname</h1>
      <p class="holder-position">Position</p>
    </header>

    <dl class="contact-list">
      <dt>Address</dt><dd>#48 Harbour Lane, Coral Bay, QLD 4701</dd>
      <dt>Office</dt><dd>041.552.3086</dd>
      <dt class="gap">Mobile</dt><dd class="gap">075.318.2649</dd>
      <dt>E-mail</dt><dd>name@brinerun.com</dd>
      <dt>Facebook</dt><dd>brinerun</dd>
      <dt>Twitter</dt><dd>brinerun</dd>
      <dt class="gap">Website</dt><dd class="gap">www.brinerun.com</dd>
      <dt>ABN</dt><dd>52 718 904 336</dd>
    </dl>

    <div class="brand">
      <span class="brand-dot"></span>
      <span class="brand-name">Brine Run</span>
    </div>
  </article>
</body>
</html>
```